Banner Pop Up Opt In Form REDESIGNS - SLEEK BLACK LOOK

Please redesign banners attached.

I am looking for a very sleek look....I do not like this collage of images on these current designs. Please keep all content same but use images that pop.

I have an acccount at www.pixmorrow-example.com or you can use your own images.

I like black background for somereason because it looks very sleek....but these designs should pop , build trust and credibility and have easy opt in form....SLEEK AND MODERN LOOK is what im looking for....

Target Market(s)

Consumers on websites

Requirements
Must have
• Please redesign banners attached.

Nice to have

Should not have

```html
<!DOCTYPE html>
<html lang="en">
<head>
<meta charset="utf-8">
<title>Opt-in Pop-up Banners</title>
<link rel="stylesheet" href="https://fonts.googleapis.com/css2?family=Open+Sans:wght@400;500;600&display=swap">
<style>
  :root {
    --page: #ffffff;
    --panel: #252321;
    --panel-deep: #151412;
    --accent: #ffa500;
    --accent-line: #f5a800;
    --text-light: #ffffff;
    --text-dark: #1c1b1a;
    --field: #ffffff;
    --field-text: #4a4a4a;
    --button: #2f7ef5;
  }
  * { box-sizing: border-box; margin: 0; padding: 0; }
  html, body {
    width: 1200px; height: 1200px; overflow: hidden;
    background: var(--page);
    font-family: "Open Sans", sans-serif;
  }
  .sheet { position: relative; width: 1200px; height: 1200px; }
  .banner {
    position: absolute;
    width: 800px; height: 688px;
    transform: scale(0.625);
    transform-origin: 0 0;
    overflow: hidden;
    background: linear-gradient(160deg, #2d2a27 0%, var(--panel) 45%, var(--panel-deep) 100%);
  }
  .banner--fitness-offer { left: 32.5px; top: 135px; }
  .banner--fitness-win { left: 636px; top: 135px; }
  .banner--hotel-win { left: 370.6px; top: 713.8px;
    background: linear-gradient(180deg, #2f2823 0%, #1f1b18 40%, #141210 100%); }
  .banner__art { position: absolute; inset: 0; width: 800px; height: 688px; }
  .headline {
    position: absolute; left: 46px; top: 32px;
    color: var(--accent); font-weight: 500; font-size: 44px; letter-spacing: 0.5px;
    white-space: nowrap;
  }
  .headline--large { font-size: 54px; top: 32px; left: 48px; letter-spacing: 1px; }
  .intro {
    position: absolute; left: 51px; top: 95px;
    color: var(--text-light); font-size: 28px; font-weight: 500; line-height: 32px;
  }
  .prize {
    position: absolute; left: 51px; top: 160px;
    color: var(--accent); font-size: 35px; font-weight: 400; white-space: nowrap;
  }
  .prize--caps { font-size: 24px; font-weight: 500; top: 174px; }
  .optin { position: absolute; left: 46px; top: 271px; width: 342px; }
  .optin__field {
    height: 52px; margin-bottom: 18px;
    background: var(--field); border-radius: 4px;
    padding-left: 14px;
    color: var(--field-text); font-size: 26px; line-height: 52px;
  }
  .optin__submit {
    height: 52px; margin-top: 3px;
    background: var(--button); border-radius: 4px;
    color: var(--text-light); font-size: 26px; line-height: 52px; text-align: center;
  }
  .note {
    position: absolute; left: 9px; top: 632px;
    color: var(--text-dark); font-size: 18.5px; line-height: 21px;
  }
</style>
</head>
<body>
<main class="sheet">

  <section class="banner banner--fitness-offer">
    <svg class="banner__art" viewBox="0 0 800 688" aria-hidden="false">
      <defs>
        <linearGradient id="gymWide" x1="0" y1="0" x2="1" y2="1">
          <stop offset="0" stop-color="#6b5a4c"/>
          <stop offset="0.5" stop-color="#4a4440"/>
          <stop offset="1" stop-color="#bdb8b2"/>
        </linearGradient>
        <linearGradient id="gymWrist" x1="0" y1="0" x2="1" y2="1">
          <stop offset="0" stop-color="#3a3734"/>
          <stop offset="0.5" stop-color="#c99a84"/>
          <stop offset="1" stop-color="#5b5753"/>
        </linearGradient>
        <linearGradient id="gymTop" x1="0" y1="0" x2="1" y2="1">
          <stop offset="0" stop-color="#8c8a6a"/>
          <stop offset="0.5" stop-color="#d8d9dc"/>
          <stop offset="1" stop-color="#c5927c"/>
        </linearGradient>
      </defs>
      <polygon fill="url(#gymWide)" points="345,624 800,169 800,688 409,688" role="img" aria-label="Close-up of a hand on an exercise bike grip wearing a smart watch"/>
      <line x1="345" y1="624" x2="800" y2="169" stroke="var(--accent-line)" stroke-width="3"/>
      <polygon fill="url(#gymWrist)" stroke="var(--accent-line)" stroke-width="3" points="368,234 531,71 696,234 531,397" role="img" aria-label="Wrists with a smart fitness watch"/>
      <polygon fill="url(#gymTop)" stroke="var(--accent-line)" stroke-width="3" points="599,0 800,0 800,134 713,216 548,52" role="img" aria-label="Person checking a smart watch"/>
      <polygon fill="var(--accent)" points="0,624 345,624 409,688 0,688"/>
    </svg>
    <h2 class="headline">WANT A GREAT OFFER?</h2>
    <p class="intro">Subscribe to our newsletter<br>and receive a complimentary</p>
    <p class="prize">Smart Fitness Watch</p>
    <form class="optin">
      <div class="optin__field">Name</div>
      <div class="optin__field">Email</div>
      <div class="optin__field">Phone</div>
      <div class="optin__submit">SUBMIT</div>
    </form>
    <p class="note">We will send you a text message with the<br>offer and instructions on how to redeem</p>
  </section>

  <section class="banner banner--fitness-win">
    <svg class="banner__art" viewBox="0 0 800 688">
      <polygon fill="url(#gymWide)" points="345,624 800,169 800,688 409,688" role="img" aria-label="Close-up of a hand on an exercise bike grip wearing a smart watch"/>
      <line x1="345" y1="624" x2="800" y2="169" stroke="var(--accent-line)" stroke-width="3"/>
      <polygon fill="url(#gymWrist)" stroke="var(--accent-line)" stroke-width="3" points="368,234 531,71 696,234 531,397" role="img" aria-label="Wrists with a smart fitness watch"/>
      <polygon fill="url(#gymTop)" stroke="var(--accent-line)" stroke-width="3" points="599,0 800,0 800,134 713,216 548,52" role="img" aria-label="Person checking a smart watch"/>
      <polygon fill="var(--accent)" points="0,624 345,624 409,688 0,688"/>
    </svg>
    <h2 class="headline headline--large">ENTER TO WIN</h2>
    <p class="intro">Subscribe to our newsletter<br>to enter to win a</p>
    <p class="prize">Smart Fitness Watch</p>
    <form class="optin">
      <div class="optin__field">Name</div>
      <div class="optin__field">Email</div>
      <div class="optin__field">Phone</div>
      <div class="optin__submit">SUBMIT</div>
    </form>
    <p class="note">We will send you a text message with the<br>offer and instructions on how to redeem</p>
  </section>

  <section class="banner banner--hotel-win">
    <svg class="banner__art" viewBox="0 0 800 688">
      <defs>
        <linearGradient id="cityNight" x1="0" y1="0" x2="1" y2="1">
          <stop offset="0" stop-color="#3a2c24"/>
          <stop offset="0.45" stop-color="#1c1916"/>
          <stop offset="0.8" stop-color="#5a4530"/>
          <stop offset="1" stop-color="#2a2220"/>
        </linearGradient>
        <linearGradient id="poolSunset" x1="0" y1="0" x2="0" y2="1">
          <stop offset="0" stop-color="#7a6a8a"/>
          <stop offset="0.45" stop-color="#e8b070"/>
          <stop offset="0.7" stop-color="#b08868"/>
          <stop offset="1" stop-color="#3c5a78"/>
        </linearGradient>
        <linearGradient id="poolDay" x1="0" y1="0" x2="1" y2="1">
          <stop offset="0" stop-color="#e8c860"/>
          <stop offset="0.5" stop-color="#a07050"/>
          <stop offset="1" stop-color="#4a8a40"/>
        </linearGradient>
      </defs>
      <polygon fill="url(#cityNight)" points="345,624 800,169 800,688 409,688" role="img" aria-label="City skyline of lit towers at dusk"/>
      <line x1="345" y1="624" x2="800" y2="169" stroke="var(--accent-line)" stroke-width="3"/>
      <polygon fill="url(#poolSunset)" stroke="var(--accent-line)" stroke-width="3" points="367,233 532,68 697,233 532,396" role="img" aria-label="Resort pool with parasols at sunset"/>
      <polygon fill="url(#poolDay)" stroke="var(--accent-line)" stroke-width="3" points="599,0 800,0 800,134 713,216 548,52" role="img" aria-label="Tropical hotel pool with loungers and palms"/>
      <polygon fill="var(--accent)" points="0,624 345,624 409,688 0,688"/>
    </svg>
    <h2 class="headline headline--large">ENTER TO WIN</h2>
    <p class="intro">Subscribe to our email list<br>Enter to win a</p>
    <p class="prize prize--caps">$500 HOTEL SAVINGS CARDS</p>
    <form class="optin">
      <div class="optin__field">Name</div>
      <div class="optin__field">Email</div>
      <div class="optin__field">Phone</div>
      <div class="optin__submit">SUBMIT</div>
    </form>
    <p class="note">We will send you a text message with the<br>offer and instructions on how to redeem</p>
  </section>

</main>
</body>
</html>
```